Workplace Safety Consultancy Business needs business card design

We need a business card for a new business providing workplace health and safety consulting called 'Worksure Path'. We will be providing small to medium sized businesses assistance with OH&S and HR matters to ensure that their employees and the public are safe in the workplace and that they are meeting their legislative requirements. Would like to see the words 'practical workplace safety solutions' on the card. Personal details on the back. It needs to be clean, smart and professional (no fluff). Would like to see a simple logo if possible as well. Have been looking at orange and black, but open to other ideas.
Updates
Thank you to those to have created designs for us so far! We are really impressed with the impact of the black and orange having now seen it. Would be great if any further designs used those colours. Cheers.

Thank you to everyone that submitted a design. Your work is of the highest quality and we had a hard decision deciding. Sorry if we didn't choose your design, but it just came down to the one that stood out to us personally. Cheers.

Target Market(s)
Small-Medium business owners in Queensland, Australia. Age 25-60 male and female. Initially targeting those in the trade type industries
Industry/Entity Type
Health
Look and feel
Each slider illustrates characteristics of the customer's brand and the style your logo design should communicate.

```html
<!DOCTYPE html>
<html lang="en">
<head>
<meta charset="utf-8">
<title>Worksure Path – Business Card</title>
<link rel="stylesheet" href="https://fonts.googleapis.com/css2?family=Open+Sans:wght@400;700;800&display=swap">
<style>
  :root {
    --page: #e9e9e9;
    --paper: #ffffff;
    --orange: #eb7622;
    --ink: #1f1f1f;
    --charcoal: #3e3e40;
    --light: #e8e8e8;
  }
  * { box-sizing: border-box; margin: 0; padding: 0; }
  html, body { width: 1200px; height: 1200px; overflow: hidden; }
  body {
    background: var(--page);
    font-family: "Open Sans", Arial, sans-serif;
    display: flex;
    flex-direction: column;
    align-items: center;
    justify-content: center;
    gap: 70px;
  }
  .card {
    width: 700px;
    height: 400px;
    background: var(--paper);
    padding: 22px;
    box-shadow: 0 10px 30px rgba(0,0,0,0.12);
  }
  .card-face {
    width: 100%;
    height: 100%;
    position: relative;
  }
  .card-front .card-face {
    background: var(--orange);
    display: flex;
    flex-direction: column;
    align-items: center;
    justify-content: center;
  }
  .brand-name {
    color: var(--ink);
    font-weight: 800;
    font-size: 52px;
    letter-spacing: 1px;
    text-transform: uppercase;
    line-height: 1;
  }
  .tagline {
    margin-top: 12px;
    color: var(--ink);
    font-weight: 700;
    font-size: 17px;
    letter-spacing: 0.5px;
    text-transform: uppercase;
  }
  .card-back .card-face {
    background: var(--charcoal);
    padding: 70px 50px;
    display: flex;
    align-items: flex-start;
    gap: 28px;
  }
  .person-name {
    color: var(--light);
    font-weight: 700;
    font-size: 24px;
    white-space: nowrap;
    padding-top: 34px;
  }
  .contact-list {
    list-style: none;
    padding-top: 38px;
  }
  .contact-item {
    display: flex;
    align-items: center;
    gap: 10px;
    color: var(--light);
    font-size: 20px;
    line-height: 30px;
  }
  .contact-icon { width: 18px; height: 18px; flex: none; }
</style>
</head>
<body>
  <section class="card card-front">
    <div class="card-face">
      <div class="brand-name">Worksure Path</div>
      <div class="tagline">‘Practical Workplace Safety Solutions’</div>
    </div>
  </section>

  <section class="card card-back">
    <div class="card-face">
      <div class="person-name">Daniel Harlow</div>
      <ul class="contact-list">
        <li class="contact-item">
          <svg class="contact-icon" viewBox="0 0 18 18" aria-hidden="true">
            <circle cx="9" cy="9" r="9" fill="#eb7622"/>
            <rect x="6" y="4" width="6" height="10" rx="1" fill="#3e3e40"/>
            <rect x="7" y="5.3" width="4" height="6" fill="#eb7622"/>
          </svg>
          0400 123 456
        </li>
        <li class="contact-item">
          <svg class="contact-icon" viewBox="0 0 18 18" aria-hidden="true">
            <circle cx="9" cy="9" r="9" fill="#eb7622"/>
            <rect x="4.5" y="6" width="9" height="6.5" fill="#3e3e40"/>
            <path d="M4.5 6 L9 10 L13.5 6" fill="none" stroke="#eb7622" stroke-width="1"/>
          </svg>
          daniel@worksurepath.com.au
        </li>
        <li class="contact-item">
          <svg class="contact-icon" viewBox="0 0 18 18" aria-hidden="true">
            <circle cx="9" cy="9" r="9" fill="#eb7622"/>
            <circle cx="9" cy="9" r="5" fill="none" stroke="#3e3e40" stroke-width="1.3"/>
            <ellipse cx="9" cy="9" rx="2.2" ry="5" fill="none" stroke="#3e3e40" stroke-width="1.1"/>
            <line x1="4" y1="9" x2="14" y2="9" stroke="#3e3e40" stroke-width="1.1"/>
          </svg>
          worksurepath.com.au
        </li>
      </ul>
    </div>
  </section>
</body>
</html>
```